High Performance Webhosting Plovix ad Banners

We are looking for a designer that can design some very high quality and eye catching animated gif ad banners in several size and shapes to suit standards for Plovix ads.
* leaderboard (728x90)
* banner (468x60)
* half banner (234x60)
* button (125x125)
* skyscraper (120x600)
* wide skyscraper (160x600)
* small rectangle (180x150)
* vertical banner (120 x 240)

The message we want to put out on these banners is as follows:

High Performance Australian Corvalo Web Hosting
VPS with SSD's
Corvalo Speed Optmisation also available
The company Name is "Bramwick"
I have attached the logo and the URL: www.bramwick-example.com.au

Target Market(s)

Corvalo webhosting, Ecommerce Webhosting

Industry/Entity Type

Plovix

Font styles to use
Sans Serif

Colors
33a6d7
0692cd
85cae6
0556a4
3176b5
cedeed

Requirements
Must have
• High quality design with animated gif if possible to catch eye.
Nice to have
• Animated gif to be more affective in getting attention.
Should not have
• No prices to be displayed.

```html
<!DOCTYPE html>
<html lang="en">
<head>
<meta charset="utf-8">
<title>Bramwick Web Hosting Banners</title>
<link rel="stylesheet" href="https://fonts.googleapis.com/css2?family=Lato:wght@400;700;900&family=Oswald:wght@500;600&display=swap">
<style>
  :root {
    --stage: #6b4729;
    --caption: #ffffff;
    --brand-blue: #33a6d7;
    --band-blue: #0692cd;
    --band-deep: #0556a4;
    --sky-mid: #85cae6;
    --sky-pale: #cedeed;
    --sky-white: #f4f9fd;
    --ink: #3a3d42;
    --tick: #3176b5;
    --button-top: #33a6d7;
    --button-bottom: #0556a4;
    --photo-light: #b9c4cf;
    --photo-dark: #4b5560;
  }
  * { box-sizing: border-box; margin: 0; padding: 0; }
  html, body { width: 1200px; height: 900px; overflow: hidden; }
  body {
    position: relative;
    background: var(--stage);
    font-family: "Lato", Arial, sans-serif;
  }
  .caption {
    position: absolute;
    color: var(--caption);
    font: 700 20px "Lato", Arial, sans-serif;
    white-space: nowrap;
  }
  .caption--vertical { right: 83px; top: 100px; }
  .caption--half { left: 101px; top: 690px; }

  .banner {
    position: absolute;
    overflow: hidden;
    background: linear-gradient(180deg, var(--sky-mid) 0%, var(--sky-white) 45%, var(--sky-pale) 100%);
  }
  .banner__band { position: absolute; left: 0; top: 0; width: 100%; }
  .brand {
    position: absolute;
    z-index: 2;
    color: var(--brand-blue);
    font-family: "Lato", Arial, sans-serif;
    font-weight: 900;
    letter-spacing: 0.5px;
    white-space: nowrap;
  }
  .headline {
    position: absolute;
    color: var(--ink);
    font-family: "Oswald", Arial, sans-serif;
    font-weight: 600;
    letter-spacing: 0.3px;
    white-space: nowrap;
  }
  .features { position: absolute; list-style: none; color: var(--ink); }
  .features li { position: relative; }
  .features svg { position: absolute; left: 0; }
  .cta {
    position: absolute;
    display: flex;
    align-items: center;
    justify-content: center;
    color: #fff;
    font-family: "Oswald", Arial, sans-serif;
    font-weight: 500;
    border-radius: 999px;
    background: linear-gradient(180deg, var(--button-top), var(--button-bottom));
    box-shadow: 0 1px 3px rgba(0,0,0,0.35);
  }
  .cta__play {
    border-radius: 50%;
    background: #fff;
    display: flex;
    align-items: center;
    justify-content: center;
  }
  .hero-photo {
    position: absolute;
    z-index: 1;
    background: linear-gradient(90deg, var(--photo-dark) 0%, var(--photo-light) 45%, var(--photo-dark) 100%);
  }

  /* vertical banner 120 x 240 */
  .banner--vertical { left: 833px; top: 135px; width: 284px; height: 568px; }
  .banner--vertical .brand { left: 0; width: 100%; text-align: center; top: 40px; font-size: 48px; }
  .banner--vertical .headline { left: 0; width: 100%; text-align: center; top: 100px; font-size: 24px; }
  .banner--vertical .features { left: 27px; top: 140px; width: 250px; font-size: 17.5px; line-height: 24px; }
  .banner--vertical .features li { padding-left: 28px; margin-bottom: 5px; }
  .banner--vertical .features svg { top: 6px; width: 14px; height: 12px; }
  .banner--vertical .cta { left: 74px; top: 342px; width: 141px; height: 31px; font-size: 15px; gap: 12px; }
  .banner--vertical .cta__play { width: 22px; height: 22px; }
  .banner--vertical .hero-photo { left: 0; top: 380px; width: 284px; height: 188px; }

  /* half banner 234 x 60 */
  .banner--half { left: 95px; top: 520px; width: 590px; height: 150px; }
  .banner--half .brand { left: 17px; top: 18px; font-size: 19px; line-height: 24px; }
  .banner--half .hero-photo { left: 35px; top: 44px; width: 260px; height: 106px; }
  .banner--half .headline { left: 335px; top: 19px; font-size: 16px; }
  .banner--half .features { left: 345px; top: 46px; width: 240px; font-size: 11px; line-height: 14px; font-weight: 700; }
  .banner--half .features li { padding-left: 15px; margin-bottom: 4px; }
  .banner--half .features svg { top: 3px; width: 9px; height: 8px; }
  .banner--half .cta { left: 470px; top: 120px; width: 80px; height: 20px; font-size: 8px; gap: 8px; }
  .banner--half .cta__play { width: 13px; height: 13px; }
</style>
</head>
<body>
  <p class="caption caption--vertical">vertical banner (120 x 240)</p>

  <section class="banner banner--vertical" aria-label="Vertical banner">
    <svg class="banner__band" viewBox="0 0 284 60" height="60" preserveAspectRatio="none" aria-hidden="true">
      <path d="M0 0H284V60C230 20 120 12 0 26Z" fill="var(--band-blue)"/>
      <path d="M0 0H284V20C200 6 90 6 0 14Z" fill="var(--band-deep)" opacity="0.5"/>
    </svg>
    <h2 class="brand">Bramwick</h2>
    <h3 class="headline">WEB HOSTING SERVICE</h3>
    <ul class="features">
      <li><svg viewBox="0 0 14 12"><path d="M1 6l4 4 8-9" fill="none" stroke="var(--tick)" stroke-width="2.4"/></svg>Australia Data-Centers</li>
      <li><svg viewBox="0 0 14 12"><path d="M1 6l4 4 8-9" fill="none" stroke="var(--tick)" stroke-width="2.4"/></svg>24X7X365</li>
      <li><svg viewBox="0 0 14 12"><path d="M1 6l4 4 8-9" fill="none" stroke="var(--tick)" stroke-width="2.4"/></svg>Support 99.9% SLA Web Design</li>
      <li><svg viewBox="0 0 14 12"><path d="M1 6l4 4 8-9" fill="none" stroke="var(--tick)" stroke-width="2.4"/></svg>Development Domain Names</li>
      <li><svg viewBox="0 0 14 12"><path d="M1 6l4 4 8-9" fill="none" stroke="var(--tick)" stroke-width="2.4"/></svg>SSL Certificates</li>
    </ul>
    <a class="cta">Learn More <span class="cta__play"><svg viewBox="0 0 10 10" width="45%" height="45%"><path d="M2 1l7 4-7 4Z" fill="var(--band-deep)"/></svg></span></a>
    <div class="hero-photo" role="img" aria-label="Smiling businessman with crossed arms in front of server racks"></div>
  </section>

  <section class="banner banner--half" aria-label="Half banner">
    <svg class="banner__band" viewBox="0 0 590 30" height="30" preserveAspectRatio="none" aria-hidden="true">
      <path d="M0 0H590V30C450 6 200 4 0 12Z" fill="var(--band-blue)"/>
    </svg>
    <h2 class="brand">Bramwick</h2>
    <div class="hero-photo" role="img" aria-label="Smiling businessman with crossed arms in front of server racks"></div>
    <h3 class="headline">WEB HOSTING SERVICE</h3>
    <ul class="features">
      <li><svg viewBox="0 0 14 12"><path d="M1 6l4 4 8-9" fill="none" stroke="var(--tick)" stroke-width="2.6"/></svg>Australia Data Centers</li>
      <li><svg viewBox="0 0 14 12"><path d="M1 6l4 4 8-9" fill="none" stroke="var(--tick)" stroke-width="2.6"/></svg>24X7X365</li>
      <li><svg viewBox="0 0 14 12"><path d="M1 6l4 4 8-9" fill="none" stroke="var(--tick)" stroke-width="2.6"/></svg>Support 99.9% SLA Web Design</li>
      <li><svg viewBox="0 0 14 12"><path d="M1 6l4 4 8-9" fill="none" stroke="var(--tick)" stroke-width="2.6"/></svg>Development Domain Names</li>
      <li><svg viewBox="0 0 14 12"><path d="M1 6l4 4 8-9" fill="none" stroke="var(--tick)" stroke-width="2.6"/></svg>SSL Certificates</li>
    </ul>
    <a class="cta">Learn More <span class="cta__play"><svg viewBox="0 0 10 10" width="45%" height="45%"><path d="M2 1l7 4-7 4Z" fill="var(--band-deep)"/></svg></span></a>
  </section>

  <p class="caption caption--half">half banner (234x60)</p>
</body>
</html>
```